Refresh look of our invoices (Excel spreadsheet which converts to PDF) to better match our new look

We have recently updated our Website and other marketing material with a new look and would like to refresh our invoice template so that it better matches our new look.  The template is an excel spreadsheet which we convert to a PDF to send out to our clients.
The main requirement is to incorporate the newer design colours and general look/feel to align with what is on our website www.corvalhill.com.au
It is extremely important that excel formula functionality and general layout are much the same although we are open to any design suggestions you might have.
Please note:
-Totals figures and news panel must remain on the first page
-We need full ability to edit embedded formulas and Excel spreadsheet is NOT to be password protected as we will only be using it internally.
-It is crucial that the second and subsequent pages can be extended (duplicated) internally to allow for larger multi page entries. Some of our clients invoices run up to 4/5 pages in length and we need the abilty to keep adding rows)
-possibility to add a "convert to PDF" button within the sheet which provides a 1 click solution to convert to PDF rather than the manual 2 step process to convert.... If that can be done, we would not want the "convert to PDF" button to show on final PDF converted version we issue to our customers.   Ideally, a single "convert to PDF and print first cover page only" in 1 single click button named 'convert to PDF & print' would be really handy.  -  (Just to explain why - we email out a PDF version of invoice to our clients and only print off first page with totals for our records)
The design for the first page can be different from the second & subsequent pages (eg first page can be more fancy with following pages more basic)

Finance Industry
Marketing

```html
<!DOCTYPE html>
<html lang="en">
<head>
<meta charset="utf-8">
<title>Recipient Created Tax Invoice – Corval Hill</title>
<link href="https://fonts.googleapis.com/css2?family=Arimo:wght@400;700&family=Michroma&family=Open+Sans:wght@300;400&display=swap" rel="stylesheet">
<style>
  :root {
    --ink: #1a1a1a;
    --band: #3a3a3a;
    --brand-green: #7ab51d;
    --soft-grey: #bdbdbd;
    --alert-red: #e0221b;
    --paper: #ffffff;
  }
  * { margin: 0; padding: 0; box-sizing: border-box; }
  html, body { width: 847px; height: 1200px; overflow: hidden; background: var(--paper); }
  body { position: relative; font-family: "Arimo", Arial, sans-serif; color: var(--ink); }
  .abs { position: absolute; }

  .sheet-count { top: 98px; right: 80px; font-size: 9px; }

  .header-band { top: 123px; left: 79px; width: 682px; height: 52px; background: var(--band); }
  .brand-name { left: 14px; top: 8px; font-family: "Open Sans", Arial, sans-serif; font-weight: 300; font-size: 32px; color: var(--paper); letter-spacing: 1px; line-height: 36px; }
  .call-block { right: 12px; top: 8px; text-align: right; font-family: "Open Sans", Arial, sans-serif; }
  .call-label { font-size: 10px; color: var(--soft-grey); letter-spacing: .3px; }
  .call-number { font-size: 22px; color: var(--brand-green); line-height: 24px; }

  .company-block { top: 189px; left: 79px; font-family: "Michroma", Arial, sans-serif; font-size: 7.5px; line-height: 12.2px; letter-spacing: .8px; text-transform: uppercase; }
  .company-block .web { color: var(--brand-green); text-transform: lowercase; }
  .company-abn { top: 290px; left: 79px; font-family: "Michroma", Arial, sans-serif; font-size: 7.5px; letter-spacing: .8px; }

  .title-bar { top: 312px; left: 79px; width: 682px; height: 18px; border-top: 3px solid var(--ink); border-bottom: 1px solid var(--ink); text-align: center; font-weight: 700; font-size: 13px; line-height: 14px; }

  .label { font-weight: 700; font-size: 9.5px; }
  .referrer-name { top: 346px; left: 119px; }
  .referrer-address { top: 369px; left: 107px; }
  .referrer-abn { top: 440px; left: 163px; }
  .invoice-date-label { top: 346px; left: 605px; }
  .invoice-date { top: 346px; left: 690px; }

  .totals { top: 890px; left: 455px; width: 306px; font-size: 11px; font-weight: 700; }
  .totals-row { display: flex; justify-content: flex-end; height: 14.4px; line-height: 14.4px; }
  .totals-row .name { width: 206px; text-align: right; padding-right: 16px; }
  .totals-row .value { width: 90px; text-align: right; padding-right: 10px; }
  .totals-row .value.negative { color: var(--alert-red); }
  .totals-total { border-top: 1px solid var(--ink); border-bottom: 2px solid var(--ink); margin-top: 2px; justify-content: space-between; height: 16px; line-height: 14px; }
  .totals-total .name { text-align: left; width: auto; padding-left: 2px; }

  .news-heading { top: 997px; left: 79px; width: 682px; text-align: center; color: var(--alert-red); font-weight: 700; font-size: 9px; }
  .news-body { top: 1011px; left: 79px; width: 682px; font-weight: 700; font-size: 9px; line-height: 14.4px; }
  .news-body .link { color: var(--brand-green); }

  .privacy-note { top: 1052px; left: 79px; width: 682px; height: 25px; border: 2px solid var(--ink); padding: 1px 3px; font-style: italic; font-size: 7px; line-height: 9.5px; }
</style>
</head>
<body>
  <div class="abs sheet-count">Sheet 1 of 2</div>

  <header class="abs header-band">
    <div class="abs brand-name">CORVAL HILL</div>
    <div class="abs call-block">
      <div class="call-label">PHONE US TODAY!</div>
      <div class="call-number">1300 555 214</div>
    </div>
  </header>

  <address class="abs company-block" style="font-style:normal">
    Corval Hill Pty Ltd<br>
    Level 12/88 Harlow Street<br>
    Melbourne<br>
    Vic 3000<br>
    P: 1300 555 214<br>
    F: 1300 555 219<br>
    <span class="web">www.corvalhill.com.au</span>
  </address>
  <div class="abs company-abn">ABN &nbsp;00 111 222 333</div>

  <h1 class="abs title-bar">RECIPIENT CREATED TAX INVOICE</h1>

  <div class="abs label referrer-name">Referrer Name:</div>
  <div class="abs label referrer-address">Referrer Address:</div>
  <div class="abs label referrer-abn">ABN: 00 000 000 000</div>
  <div class="abs label invoice-date-label">Invoice Date:</div>
  <div class="abs label invoice-date">07-Sep-13</div>

  <section class="abs totals">
    <div class="totals-row"><span class="name">Upfront</span><span class="value">$3,000.00</span></div>
    <div class="totals-row"><span class="name">Trail</span><span class="value">$202.26</span></div>
    <div class="totals-row"><span class="name">Adjustments</span><span class="value negative">-$50.00</span></div>
    <div class="totals-row"><span class="name">GST</span><span class="value">$315.24</span></div>
    <div class="totals-row totals-total"><span class="name">TOTAL AMOUNT DEPOSITED</span><span class="value">$3,467.50</span></div>
  </section>

  <div class="abs news-heading">* CORVAL LINK - Referral management software *</div>
  <p class="abs news-body">
    The Corval Link software provides you with a fully compliant referral process that is supported by the lenders. Apart from making new<br>
    referrals, you can also read lender updates on deal progress and lodge enquires for outstanding commission payments. You can login by going<br>
    to the dedicated Corval Link website at: <span class="link">www.corvallink.com.au</span>
  </p>

  <p class="abs privacy-note">This report contains confidential client information. Disclosure of customer information such as loan details and lenders to third parties may be a contravention of the Privacy Act, unless they are authorised to receive such details.</p>
</body>
</html>
```